Namecard, letterhead & envelope
Executive Search firm
Project: Namecard, letterhead & envelope
Namecard, letterhead & envelope - Employment
Creative Brief
Professional
Derek Lim Wei Khong
President & CEO
548 Harbour Lane #05-07 Crestview Singapore 208463
dereklim@velquarepartners.example
www.velquarepartners.example
27K9053
If you think you can design a better logo, please feel free to do so. Your design should be clean, classy & professional looking. We are in the high-end headhuntng business. Background colour is white and preferably 2 colour, i.e. black plus one other colour, either gold or colour close to earth tone. But I am open to orange, yellow, brown.

```html
<!DOCTYPE html>
<html lang="en">
<head>
<meta charset="utf-8">
<title>Velquare Partners – Stationery Set</title>
<link href="https://fonts.googleapis.com/css2?family=Arimo:wght@400;700&family=Oswald:wght@500&display=swap" rel="stylesheet">
<style>
  :root {
    --brand-red: #c4161c;
    --ink: #111111;
    --paper: #ffffff;
    --rule-grey: #d4d4d4;
    --label: #f4f4f4;
  }
  html, body { margin: 0; padding: 0; overflow: hidden; }
  .canvas {
    position: relative;
    width: 1200px; height: 847px; overflow: hidden;
    background: linear-gradient(155deg, #ffffff 8%, #d9d9d9 38%, #6a6a6a 68%, #1a1a1a 92%);
    font-family: "Arimo", Arial, sans-serif;
    color: var(--ink);
  }
  .sheet { position: absolute; background: var(--paper); box-shadow: 0 2px 8px rgba(0,0,0,.25); }

  .brand-name { position: absolute; font-weight: 700; color: var(--ink); display: flex; align-items: center; gap: 8px; letter-spacing: -0.5px; }
  .brand-name .mark { width: 14px; height: 14px; background: var(--brand-red); flex: none; }

  .red-band { position: absolute; left: 0; right: 0; background: var(--brand-red); color: #fff; font-weight: 700; }

  /* Letterhead */
  .letterhead { left: 12px; top: 12px; width: 521px; height: 816px; }
  .letterhead .brand-name { left: 180px; top: 34px; font-size: 44px; }
  .letterhead .licence { position: absolute; right: 24px; top: 30px; font-size: 11px; }
  .letterhead .contact-rule {
    position: absolute; left: 40px; right: 40px; top: 100px; height: 22px;
    border-top: 3px solid var(--rule-grey); border-bottom: 3px solid var(--rule-grey);
    font-size: 13px; color: #666; text-align: center; line-height: 22px; letter-spacing: .3px;
  }
  .letterhead .address { position: absolute; left: 0; right: 0; bottom: 62px; text-align: center; font-size: 16px; font-weight: 700; }
  .letterhead .red-band { bottom: 28px; height: 28px; line-height: 28px; text-align: center; font-size: 17px; }

  /* Envelope */
  .envelope { left: 600px; top: 67px; width: 576px; height: 288px; }
  .envelope .brand-name { left: 18px; top: 16px; font-size: 40px; }
  .envelope .window {
    position: absolute; left: 12px; top: 144px; width: 281px; height: 77px;
    border-radius: 12px; background: linear-gradient(180deg, #e9e9e9, #fafafa);
    border: 4px solid #c8c8c8; box-sizing: border-box; box-shadow: inset 0 2px 4px rgba(0,0,0,.2);
  }
  .envelope .red-band { top: 247px; height: 34px; line-height: 34px; text-align: right; padding-right: 14px; font-size: 18px; }

  .section-label { position: absolute; font-family: "Oswald", Impact, sans-serif; font-weight: 500; color: var(--label); font-size: 34px; letter-spacing: 1px; line-height: 1; }
  .label-envelope { left: 846px; top: 364px; }
  .label-letterhead { left: 546px; top: 444px; writing-mode: vertical-rl; }
  .label-card { left: 806px; top: 596px; }

  /* Business card */
  .business-card { left: 804px; top: 643px; width: 199px; height: 130px; font-size: 5.5px; }
  .business-card .holder { position: absolute; left: 8px; top: 6px; font-weight: 700; font-size: 6.5px; }
  .business-card .title { position: absolute; left: 8px; top: 14px; }
  .business-card .address { position: absolute; right: 8px; top: 6px; text-align: right; line-height: 1.35; }
  .business-card .brand-name { left: 8px; top: 42px; font-size: 22px; gap: 4px; }
  .business-card .brand-name .mark { width: 8px; height: 8px; }
  .business-card .red-line { position: absolute; left: 8px; top: 70px; width: 80px; height: 5px; background: var(--brand-red); }
  .business-card .web { position: absolute; left: 30px; top: 90px; color: var(--brand-red); font-weight: 700; }
  .business-card .phones { position: absolute; right: 8px; top: 82px; text-align: right; color: var(--brand-red); line-height: 1.35; }
  .business-card .licence { position: absolute; left: 8px; bottom: 6px; }
  .business-card .email { position: absolute; right: 8px; bottom: 6px; }
</style>
</head>
<body>
<div class="canvas">

  <section class="sheet letterhead">
    <div class="licence">License No. 27K9053</div>
    <div class="brand-name"><span class="mark"></span>Velquare</div>
    <div class="contact-rule">Phone +65-6400-2150 // Cell +65-9211-2150 // Fax +65-6377-2150</div>
    <div class="address">548 Harbour Lane #05-07 Crestview Singapore 208463</div>
    <div class="red-band">www.velquarepartners.example</div>
  </section>

  <section class="sheet envelope">
    <div class="brand-name"><span class="mark"></span>Velquare</div>
    <div class="window"></div>
    <div class="red-band">www.velquarepartners.example</div>
  </section>

  <div class="section-label label-envelope">ENVELOPE</div>
  <div class="section-label label-letterhead">LETTERHEAD</div>
  <div class="section-label label-card">BUSINESS CARD</div>

  <section class="sheet business-card">
    <div class="holder">Derek Lim Wei Khong</div>
    <div class="title">President &amp; CEO</div>
    <div class="address">548 Harbour Lane<br>#05-07 Crestview<br>Singapore 208463</div>
    <div class="brand-name"><span class="mark"></span>Velquare</div>
    <div class="red-line"></div>
    <div class="web">www.velquarepartners.example</div>
    <div class="phones">Phone +65-6400-2150<br>Cell +65-9211-2150<br>Fax +65-6377-2150</div>
    <div class="licence">Licence 27K9053</div>
    <div class="email">dereklim@velquarepartners.example</div>
  </section>

</div>
</body>
</html>
```